Business Card - Existing Logo & Branding copied to Business Card Format

We are looking for a designer to help with designing a two sided business card for us. We sell a web based software platform that helps people sell access to online training.
We have an existing logo and recently completed a design project here on draft hive to have someone design a nice trade show booth for us (also attached file for that design as well as our logo). We really like the look and feel of the tradeshow booth design. The fonts, colors, etc all work for us. We are hoping someone can create something very similar just in business card format.
Should be pretty straight forward hopefully....
On one side we want the logo, employee name, email address, phone and fax. On the other side we would like the text "transform your organizations training, revenue products = revenue" - See the attached PSD for what we want that to look like.
You can also see our website at www.tutorvane.com for an example of our branding.
We are open to ideas, have done several projects on draft hive and love when designers come up with creative approaches that are even better then what we envisioned.
Software

```html
<!DOCTYPE html>
<html lang="en">
<head>
<meta charset="utf-8">
<title>TutorVane Business Card</title>
<link rel="stylesheet" href="https://fonts.googleapis.com/css2?family=Arvo:wght@700&family=Roboto:wght@500;700&display=swap">
<style>
  :root {
    --backdrop: #3a3a3a;
    --card-light: #f6f6f6;
    --card-shade: #e4e4e4;
    --brand-red: #b11f2b;
    --brand-red-deep: #961a24;
    --ink-dark: #3c3c3c;
    --ink-grey: #5b5b5b;
    --bar-grey: #6e6e6e;
    --white: #ffffff;
  }
  * { box-sizing: border-box; margin: 0; padding: 0; }
  html, body {
    width: 1057px;
    height: 1200px;
    overflow: hidden;
    background: var(--backdrop);
  }
  .card {
    position: absolute;
    left: 25px;
    width: 1002px;
    height: 541px;
    overflow: hidden;
    background: linear-gradient(180deg, var(--card-light) 0%, var(--card-shade) 100%);
  }
  .card--front { top: 25px; }
  .card--back { top: 611px; }

  /* Front */
  .front-panel { position: absolute; inset: 0; }
  .contact {
    position: absolute;
    left: 0;
    top: 0;
    width: 530px;
    text-align: center;
    color: var(--white);
    font-family: "Arvo", Georgia, serif;
    font-weight: 700;
  }
  .contact__name {
    position: absolute;
    left: 0; width: 530px;
    top: 142px;
    font-size: 41px;
    letter-spacing: 1px;
  }
  .contact__line {
    position: absolute;
    left: 0; width: 530px;
    font-size: 21px;
    line-height: 30px;
  }
  .contact__phone { top: 238px; }
  .contact__email { top: 296px; }
  .contact__address { top: 352px; }

  .brand {
    position: absolute;
    display: flex;
    align-items: center;
    gap: 14px;
    font-family: "Roboto", Arial, sans-serif;
    font-weight: 500;
    color: var(--ink-dark);
  }
  .brand__square {
    width: 44px;
    height: 44px;
    background: var(--brand-red);
  }
  .brand--front { left: 618px; top: 240px; font-size: 44px; }
  .brand--back { left: 47px; top: 195px; font-size: 44px; }

  /* Back */
  .feature-band {
    position: absolute;
    left: 0; right: 0;
    top: 141px;
    height: 255px;
    background: linear-gradient(180deg, #f3f3f3, #e9e9e9);
  }
  .feature-bar {
    position: absolute;
    left: 0; right: 0;
    height: 12px;
    background: var(--bar-grey);
  }
  .feature-bar--top { top: 135px; }
  .feature-bar--bottom { top: 390px; }

  .idea-art {
    position: absolute;
    left: 610px;
    top: 100px;
    width: 392px;
    height: 290px;
    background: linear-gradient(135deg, #fafafa 0%, #c9c9c9 55%, #7d7d7d 100%);
  }
  .pointer-arrow {
    position: absolute;
    left: 430px;
    top: 228px;
  }
  .tagline-lead {
    position: absolute;
    left: 43px;
    top: 298px;
    font-family: "Roboto", Arial, sans-serif;
    font-weight: 700;
    font-size: 22px;
    color: var(--ink-grey);
  }
  .tagline {
    position: absolute;
    left: 43px;
    top: 338px;
    font-family: "Arvo", Georgia, serif;
    font-weight: 700;
    font-size: 29px;
    color: var(--brand-red);
    white-space: nowrap;
  }
  .tagline__result { color: var(--ink-grey); }
</style>
</head>
<body>

<section class="card card--front">
  <svg class="front-panel" width="1002" height="541" viewBox="0 0 1002 541">
    <defs>
      <linearGradient id="redPanel" x1="0" y1="0" x2="0" y2="1">
        <stop offset="0" stop-color="#b52230"/>
        <stop offset="1" stop-color="#961a24"/>
      </linearGradient>
    </defs>
    <path d="M0 0 H516 C588 150 596 380 518 541 H0 Z" fill="url(#redPanel)"/>
  </svg>

  <div class="contact">
    <p class="contact__name">DANIEL HARTLEY</p>
    <p class="contact__line contact__phone">800-555-0147</p>
    <p class="contact__line contact__email">info@tutorvane.com</p>
    <p class="contact__line contact__address">1180 Alder Bay Rd #210<br>Portland, OR 97209</p>
  </div>

  <div class="brand brand--front">
    <span class="brand__square"></span>
    <span class="brand__name">TutorVane</span>
  </div>
</section>

<section class="card card--back">
  <div class="feature-band"></div>
  <div class="feature-bar feature-bar--top"></div>
  <div class="feature-bar feature-bar--bottom"></div>

  <div class="idea-art" role="img" aria-label="Illustration of a light bulb equal to a hand holding stacks of banknotes"></div>

  <div class="brand brand--back">
    <span class="brand__square"></span>
    <span class="brand__name">TutorVane</span>
  </div>

  <svg class="pointer-arrow" width="80" height="90" viewBox="0 0 80 90">
    <path d="M8 8 C40 10 56 30 50 66" fill="none" stroke="#777" stroke-width="4" stroke-linecap="round"/>
    <path d="M38 58 L50 80 L62 58 Z" fill="#777"/>
  </svg>

  <p class="tagline-lead">Transform Your Organization's</p>
  <p class="tagline">TRAINING, REVENUE PRODUCTS <span class="tagline__result">= REVENUE</span></p>
</section>

</body>
</html>
```